Harborline Energy - needs a business card

Harborline Energy is a U.S. based diesel sourcing and distribution company that supports American oil & gas fields through providing quality product and consistent services.

Target Market(s)

Oil and Gas

Contact Information for Business Card

The background of the card must be white to ensure the logo pops.

Font styles to use
Serif
Sans Serif

Colors

Designer to choose colors to be used in the design.

Requirements
Must have
• Front of Card: Tag line: Harborline Energy, Powering America's Oil & Gas fields.
• Not sure if you guys do this part but just in case...
• Dale Menschow
• Owner/CEO
• C:555.318.4076
• E:Dmenschow@harborlineenergy.example
• W:Harborlineenergy.example
• Locations: Servicing the Powder River, DJ basin and Bakken formations.
• Back of Card: " Frac fueling is what we do. We understand how important diesel fuel is to your operation, which is why our main service line is Frac fueling. We assure our supply and stand by our service"

```html
<!DOCTYPE html>
<html lang="en">
<head>
<meta charset="utf-8">
<title>Harborline Energy – Business Card</title>
<link rel="stylesheet" href="https://fonts.googleapis.com/css2?family=Montserrat:wght@400;600;700&display=swap">
<style>
  :root {
    --navy: #1e2d5c;
    --red: #c0282d;
    --text-grey: #6b6b6b;
    --card: #f1f1ef;
    --backdrop: #d6d6d6;
  }
  * { margin: 0; padding: 0; box-sizing: border-box; }
  html, body { width: 1200px; height: 1200px; overflow: hidden; }
  body {
    background: var(--backdrop);
    font-family: "Montserrat", Arial, sans-serif;
    position: relative;
  }
  .card {
    position: absolute;
    left: 226px;
    width: 780px;
    height: 451px;
    background: var(--card);
    overflow: hidden;
  }
  .card-front { top: 106px; }
  .card-back { top: 638px; }

  .brand {
    position: absolute;
    display: flex;
    align-items: center;
    gap: 9px;
    transform: translateX(-50%);
    white-space: nowrap;
  }
  .brand-dot {
    width: 22px; height: 22px;
    border-radius: 50%;
    background: var(--navy);
    flex: none;
  }
  .brand-name {
    font-weight: 700;
    font-size: 23px;
    color: var(--navy);
    letter-spacing: 0.3px;
  }
  .card-front .brand { left: 196px; top: 198px; }
  .card-back .brand { left: 390px; top: 190px; }
  .card-back .brand-dot { width: 26px; height: 26px; }
  .card-back .brand-name { font-size: 27px; }

  .divider {
    position: absolute;
    left: 368px; top: 115px;
    width: 2px; height: 220px;
    background: var(--red);
  }
  .contact-block {
    position: absolute;
    left: 388px; top: 113px;
    right: 20px;
    color: var(--text-grey);
    font-size: 17px;
  }
  .person-name {
    font-size: 27px;
    font-weight: 600;
    color: var(--navy);
    line-height: 1.1;
  }
  .person-name .first { color: var(--red); }
  .person-title {
    font-size: 17px;
    color: var(--red);
    margin-top: 4px;
  }
  .service-area {
    margin-top: 20px;
    line-height: 26px;
  }
  .contact-list {
    list-style: none;
    margin-top: 22px;
    line-height: 25px;
    font-size: 16px;
  }
  .contact-list li { display: flex; align-items: center; gap: 5px; white-space: nowrap; }
  .contact-list svg { width: 13px; height: 13px; flex: none; }

  .tagline {
    position: absolute;
    left: 0; right: 0; top: 388px;
    text-align: center;
    font-size: 18px;
    color: var(--text-grey);
  }
  .service-statement {
    position: absolute;
    left: 70px; right: 70px; top: 346px;
    text-align: center;
    font-size: 18px;
    line-height: 23px;
    color: var(--text-grey);
  }
</style>
</head>
<body>
  <section class="card card-front">
    <div class="brand">
      <span class="brand-dot"></span>
      <span class="brand-name">Harborline Energy</span>
    </div>
    <div class="divider"></div>
    <div class="contact-block">
      <h1 class="person-name"><span class="first">DALE</span> MENSCHOW</h1>
      <p class="person-title">Owner/CEO</p>
      <p class="service-area">Servicing the Powder River<br>DJ basin and Bakken formations</p>
      <ul class="contact-list">
        <li>
          <svg viewBox="0 0 16 16" aria-hidden="true"><path fill="var(--navy)" d="M3.6 1.2l2.3 2.6-1.4 1.6c.9 2 2.4 3.5 4.4 4.5l1.6-1.4 2.6 2.3-1.2 2.3C7.2 12.8 3.4 9 1.2 4.2z"/></svg>
          555.318.4076
        </li>
        <li>
          <svg viewBox="0 0 16 16" aria-hidden="true"><rect x="1" y="3" width="14" height="10" fill="var(--red)"/><path d="M1 3l7 6 7-6" stroke="var(--card)" stroke-width="1.3" fill="none"/></svg>
          Dmenschow@harborlineenergy.example
        </li>
        <li>
          <svg viewBox="0 0 16 16" aria-hidden="true"><circle cx="8" cy="8" r="7" fill="var(--navy)"/><path d="M1 8h14M8 1v14M3 4.5h10M3 11.5h10" stroke="var(--card)" stroke-width="0.9" fill="none"/><ellipse cx="8" cy="8" rx="3" ry="7" stroke="var(--card)" stroke-width="0.9" fill="none"/></svg>
          www.Harborlineenergy.example
        </li>
      </ul>
    </div>
    <p class="tagline">Harborline Energy, Powering America's Oil &amp; Gas fields</p>
  </section>

  <section class="card card-back">
    <div class="brand">
      <span class="brand-dot"></span>
      <span class="brand-name">Harborline Energy</span>
    </div>
    <p class="service-statement">Frac fueling is what we do. We understand how important diesel fuel is to your operation, which is why our main service line is Frac fueling. We assure our supply and stand by our service.</p>
  </section>
</body>
</html>
```